Landing page design for secure cloud backup web application

We would like a landing page design for our web application. Our app allows users to securely save their data in the cloud using their existing storage providers, such as tidLoft, Keg, Velmora Sky Locker, Pintaro stash and Quelvix Sole vault.
We make it extremely easy for individual users and small businesses to deploy sophisticated client-side encryption without having to worry about the technical complexity inherent in such solutions.
We already have the logo design done - I am attaching the logo file. We also have a preliminary website drafted at www.pemraq.test
I need a good color scheme, typography, layout, along with templates for 'help', 'about', 'privacy notice', 'legal' and such typical sub-pages
The design should be uncluttered, clean and minimalist

Target Market(s)

Individuals and medium/small businesses that are conscious about the security of their data in the cloud

Coding

Coded - Design and coding required

Number of Pages Required

4 page

Font styles to use
Sans Serif

Requirements
Must have
• Section where I describe the product along with pictures/images
• section for explainer video on main page
• FAQ section
• Help section
• Legal/privacynotice/terms of use section
• feedback section
Nice to have
• see existing draft site www.pemraq.test for content guidelines only.
• see attached logo files for color scheme guidelines - I am willing to accept change in the logo color if necessary to create a better web site look and feel
• Fonts on page should match font in the logo

```html
<!DOCTYPE html>
<html lang="en">
<head>
<meta charset="utf-8">
<title>Pemraq — Keep your data private</title>
<link rel="stylesheet" href="https://fonts.googleapis.com/css2?family=Montserrat:wght@400;500;600&family=Roboto:wght@400;500&display=swap">
<style>
:root{
  --orange:#f7931e;
  --ink:#3c3c3c;
  --muted:#777;
  --slate:#555556;
  --panel:#555555;
  --light:#ececec;
  --foot-nav:#3b3b3b;
  --foot:#313131;
  --legal:#494949;
  --white:#fff;
  --line:#dcdcdc;
}
*{box-sizing:border-box;margin:0;padding:0}
html,body{width:1200px;height:2539px;overflow:hidden}
body{font-family:"Roboto",Arial,sans-serif;color:var(--ink);background:var(--white)}
.wrap{width:980px;margin:0 auto;position:relative}
h1,h2,h3,h4{font-family:"Montserrat",Arial,sans-serif;font-weight:400}

/* header */
.site-header{height:95px}
.site-header .wrap{display:flex;align-items:center;height:95px}
.brand{display:flex;align-items:center;gap:10px;font-family:"Montserrat",sans-serif;font-weight:600;font-size:30px;color:#4a4a4a;letter-spacing:1px}
.brand-dot{width:28px;height:28px;border-radius:50%;background:var(--orange)}
.main-nav{margin-left:auto;display:flex;align-items:center;gap:44px;font-family:"Montserrat",sans-serif;font-size:12px;color:#666;text-transform:uppercase}
.main-nav .current{color:#222}
.btn{display:inline-flex;align-items:center;justify-content:center;background:var(--orange);color:var(--white);font-family:"Montserrat",sans-serif;font-size:12px;text-transform:uppercase;border-radius:3px}
.main-nav .btn{width:160px;height:38px;margin-left:-4px}

/* hero */
.hero{height:532px;position:relative;background:linear-gradient(180deg,#2d2f33 0%,#3a3a3c 40%,#4a4640 70%,#2b2a28 100%);text-align:center;color:var(--white)}
.hero-copy{position:absolute;left:0;right:0;top:217px}
.hero h1{font-size:31px;font-weight:500;margin-bottom:14px}
.hero p{font-size:20px;color:var(--orange);line-height:32px;width:900px;margin:0 auto}
.slider-dots{position:absolute;top:487px;left:0;right:0;display:flex;justify-content:center;gap:6px}
.slider-dots span{width:8px;height:8px;border-radius:50%;background:#666}
.slider-dots .on{background:var(--orange)}

/* features */
.features{height:301px;padding-top:38px}
.features .wrap{display:grid;grid-template-columns:496px 484px;row-gap:34px}
.feature{display:flex;gap:25px}
.feature-icon{flex:0 0 80px;height:80px;border-radius:50%;background:var(--slate);display:flex;align-items:center;justify-content:center}
.feature h3{font-size:21px;color:#444;margin:4px 0 10px;text-transform:uppercase}
.feature p{font-size:12px;color:var(--muted);line-height:25px;width:370px}

/* apps */
.apps{height:145px;background:var(--light);text-align:center;padding-top:30px}
.apps h2{font-size:20px;color:#444;display:flex;justify-content:center;align-items:center;gap:12px;text-transform:uppercase}
.apps p{font-size:12px;color:var(--muted);margin:14px 0 12px}
.app-list{display:flex;justify-content:center;gap:22px;font-size:13px;color:#666;list-style:none}
.app-list li{display:flex;align-items:center;gap:7px}

/* tagline band */
.tagline{height:85px;background:var(--slate);color:var(--white);display:flex;align-items:center;justify-content:center}
.tagline h2{font-size:30px;font-weight:500}

/* product */
.product{height:310px;background:var(--orange);position:relative}
.product .wrap{display:flex;height:310px}
.laptop{flex:0 0 500px;width:500px;margin-top:34px;height:280px}
.laptop-screen{width:420px;height:266px;margin-left:48px;border-radius:12px 12px 0 0;background:linear-gradient(180deg,#2a2a2a 0%,#3a3a3a 5%,#f3efe2 10%,#f6f2e6 90%,#2a2a2a 93%,#2a2a2a 100%)}
.laptop-base{width:500px;height:14px;border-radius:0 0 8px 8px;background:linear-gradient(180deg,#e2e3e5 0%,#b8b9bb 60%,#8f9092 100%)}
.product-copy{flex:0 0 466px;margin-left:4px;padding-top:46px;color:var(--white)}
.product-copy p{font-size:15.5px;line-height:28.5px}
.providers{display:flex;flex-wrap:nowrap;gap:16px;margin-top:30px;font-size:13px;font-weight:500;color:var(--white);white-space:nowrap}
.providers li{list-style:none;display:flex;align-items:center;gap:7px;flex-shrink:0}
.providers .mark{width:13px;height:13px;background:var(--white)}

/* faq + help */
.support{height:565px;padding-top:48px}
.support .wrap{display:flex;justify-content:space-between}
.faq{width:562px}
.faq h2{font-size:20px;color:#444;text-transform:uppercase;margin-bottom:10px}
.faq-list{list-style:none}
.faq-item{border-bottom:1px solid var(--line);padding:18px 0 18px 2px}
.faq-item:first-child{padding-top:6px}
.faq-q{display:flex;justify-content:space-between;align-items:center;font-family:"Montserrat",sans-serif;font-size:15px;color:#444}
.faq-a{font-size:11.5px;color:var(--muted);line-height:22px;margin-top:6px;padding-right:10px}
.aside{width:391px;margin-top:21px}
.card{background:var(--panel);color:var(--white);padding:28px 26px}
.card h3{font-size:21px;margin-bottom:14px}
.help{height:270px}
.help p{font-size:12px;color:#ddd;line-height:25px}
.help .btn{width:130px;height:48px;font-size:13px;margin-top:20px}
.contact{height:182px;margin-top:13px;padding-top:24px}
.contact ul{list-style:none}
.contact li{display:flex;align-items:center;gap:14px;font-size:14px;margin-bottom:14px}
.contact .ico{width:40px;height:40px;border-radius:50%;background:var(--orange);display:flex;align-items:center;justify-content:center}

/* feedback */
.feedback{height:215px;background:var(--light);padding-top:32px}
.feedback .wrap{display:flex;justify-content:space-between}
.quote{width:310px}
.quote .mark{font-family:Georgia,serif;font-size:40px;color:#666;line-height:24px;height:24px}
.quote p{font-size:12px;color:#444;line-height:22px;margin-top:6px;height:78px}
.quote cite{display:block;border-top:2px solid #d8d8d8;padding-top:10px;font-style:normal;font-size:12px;color:var(--orange)}

/* footer */
.footer-nav{height:60px;background:var(--foot-nav);display:flex;align-items:center;justify-content:center;gap:50px;font-family:"Montserrat",sans-serif;font-size:12px;color:var(--white);text-transform:uppercase}
.footer-main{height:105px;background:var(--foot);text-align:center;padding-top:26px}
.social{display:flex;justify-content:center;gap:8px}
.social span{width:24px;height:24px;border-radius:50%}
.copyright{font-size:11px;color:#777;margin-top:12px}
.legal{height:126px;background:var(--legal);padding-top:20px;position:relative}
.legal h4{font-family:"Roboto",sans-serif;font-size:11px;color:#ccc;text-transform:uppercase;margin-bottom:6px}
.legal p{font-size:10.5px;color:#8d8d8d;line-height:18px}
.legal .code{position:absolute;right:14px;top:10px;font-size:11px;color:#ddd}
</style>
</head>
<body>

<header class="site-header">
  <div class="wrap">
    <div class="brand"><span class="brand-dot"></span>PEMRAQ</div>
    <nav class="main-nav">
      <span class="current">Home</span>
      <span>Learn more/FAQ</span>
      <span>Contact</span>
      <span>Log in</span>
      <span class="btn">Sign up free</span>
    </nav>
  </div>
</header>

<section class="hero" role="img" aria-label="Night-time city skyline photograph seen from above">
  <div class="hero-copy">
    <h1>Keep your data private without breaking a sweat</h1>
    <p>Pemraq has a simple vision. Your data belongs to you and no one else.&nbsp; We make it really easy to keep it that way.</p>
  </div>
  <div class="slider-dots"><span></span><span></span><span class="on"></span><span></span></div>
</section>

<section class="features">
  <div class="wrap">
    <div class="feature">
      <div class="feature-icon"><svg width="32" height="30" viewBox="0 0 32 30"><path d="M16 29 3 16C-1 12 1 3 8 3c4 0 6 3 8 5 2-2 4-5 8-5 7 0 9 9 5 13Z" fill="#fff"/></svg></div>
      <div><h3>Use your cloud</h3><p>Pemraq lets you use the accounts you you already have and trust, such as Keg, tidLoft, Velmora Sky Locker, Quelvix Sole vault and Pintaro stash</p></div>
    </div>
    <div class="feature">
      <div class="feature-icon"><svg width="10" height="32" viewBox="0 0 10 32"><rect x="1" y="0" width="8" height="21" rx="3" fill="#fff"/><circle cx="5" cy="28" r="4" fill="#fff"/></svg></div>
      <div><h3>Zero knowledge</h3><p>When it comes to data security, zero knowledge is a good thing. No one, including Pemraq can decipher or read your data. Yet, if you forget your password, we can reset it so you will never lose your data.</p></div>
    </div>
    <div class="feature">
      <div class="feature-icon"><svg width="30" height="36" viewBox="0 0 30 36" fill="none" stroke="#fff" stroke-width="2.5" stroke-linejoin="round"><path d="M10 20V5a3 3 0 0 1 6 0v10l8 2c3 1 4 3 3 6l-2 10H12L5 24c-1-2 1-4 3-3Z"/></svg></div>
      <div><h3>Easy to use</h3><p>Pemraq is completely browser based. So there is no software to install, no updates to perform. Just point your browser to a url and go.</p></div>
    </div>
    <div class="feature">
      <div class="feature-icon"><svg width="24" height="34" viewBox="0 0 24 34"><path d="M12 0a12 12 0 0 1 12 12c0 9-12 22-12 22S0 21 0 12A12 12 0 0 1 12 0Z" fill="#fff"/><circle cx="12" cy="12" r="4.5" fill="#555556"/></svg></div>
      <div><h3>Access anywhere</h3><p>Your data is accessible from anywhere you can use a browser and access the internet.</p></div>
    </div>
  </div>
</section>

<section class="apps">
  <h2><svg width="28" height="22" viewBox="0 0 28 22"><rect x="1" y="1" width="26" height="20" rx="2" fill="none" stroke="#f7931e" stroke-width="2"/><path d="M4 18 11 10l5 5 3-3 6 6Z" fill="#f7931e"/><circle cx="20" cy="6" r="2.5" fill="#f7931e"/></svg>Multiple apps</h2>
  <p>Pemraq has multiple apps that allow you handle your most sensitive data with complete privacy and ease.</p>
  <ul class="app-list">
    <li><svg width="14" height="14" viewBox="0 0 14 14"><path d="M14 0 0 6l5 2 1 6 2-4 4 3Z" fill="#f7931e"/></svg>Passwords</li>
    <li><svg width="14" height="14" viewBox="0 0 14 14"><path d="M14 0 0 6l5 2 1 6 2-4 4 3Z" fill="#f7931e"/></svg>Coin keys</li>
    <li><svg width="14" height="14" viewBox="0 0 14 14"><path d="M14 0 0 6l5 2 1 6 2-4 4 3Z" fill="#f7931e"/></svg>Secure notes</li>
    <li><svg width="14" height="14" viewBox="0 0 14 14"><path d="M14 0 0 6l5 2 1 6 2-4 4 3Z" fill="#f7931e"/></svg>Data backups</li>
  </ul>
</section>

<section class="tagline"><h2>PEMRAQ Data privacy simplified</h2></section>

<section class="product">
  <div class="wrap">
    <div class="laptop" role="img" aria-label="Laptop showing the Pemraq secure storage file browser">
      <div class="laptop-screen"></div>
      <div class="laptop-base"></div>
    </div>
    <div class="product-copy">
      <p>You have data you want to keep to yourself. You want it safe in the cloud so you can get at it anywhere. You don't want to mess with encryption keys yet you want to keep hackers and snoops out. You know it shouldn't be so hard.<br>You're right.</p>
      <ul class="providers">
        <li><span class="mark"></span>tidLoft</li>
        <li>Velmora Sky Locker</li>
        <li>Pintaro stash</li>
        <li>Quelvix Sole vault</li>
      </ul>
    </div>
  </div>
</section>

<section class="support">
  <div class="wrap">
    <div class="faq">
      <h2>FAQ</h2>
      <ul class="faq-list">
        <li class="faq-item">
          <div class="faq-q">1 Where is my data stored?<svg width="14" height="14" viewBox="0 0 14 14"><circle cx="7" cy="7" r="7" fill="#444"/><rect x="3.5" y="6" width="7" height="2" fill="#fff"/></svg></div>
          <p class="faq-a">Your data is stored on your accounts on two or more of the following storage providers - Keg, tidLoft, Pintaro stash, Quelvix Sole vault and Velmora Sky Locker. Pemraq does not provide storage.</p>
        </li>
        <li class="faq-item"><div class="faq-q">2 How do you ensure that no one else can see my data?<svg width="14" height="14" viewBox="0 0 14 14"><circle cx="7" cy="7" r="7" fill="#444"/><path d="M3.5 6h7v2h-7zM6 3.5h2v7H6z" fill="#fff"/></svg></div></li>
        <li class="faq-item"><div class="faq-q">3 So does that mean I need to remember encryption keys for my files?<svg width="14" height="14" viewBox="0 0 14 14"><circle cx="7" cy="7" r="7" fill="#444"/><path d="M3.5 6h7v2h-7zM6 3.5h2v7H6z" fill="#fff"/></svg></div></li>
        <li class="faq-item"><div class="faq-q">4 So how are you different from other client-side solutions?<svg width="14" height="14" viewBox="0 0 14 14"><circle cx="7" cy="7" r="7" fill="#444"/><path d="M3.5 6h7v2h-7zM6 3.5h2v7H6z" fill="#fff"/></svg></div></li>
        <li class="faq-item"><div class="faq-q">5 This sounds complicated.<svg width="14" height="14" viewBox="0 0 14 14"><circle cx="7" cy="7" r="7" fill="#444"/><path d="M3.5 6h7v2h-7zM6 3.5h2v7H6z" fill="#fff"/></svg></div></li>
        <li class="faq-item"><div class="faq-q">6 So what does it cost?<svg width="14" height="14" viewBox="0 0 14 14"><circle cx="7" cy="7" r="7" fill="#444"/><path d="M3.5 6h7v2h-7zM6 3.5h2v7H6z" fill="#fff"/></svg></div></li>
        <li class="faq-item"><div class="faq-q">7 Where is my data stored?<svg width="14" height="14" viewBox="0 0 14 14"><circle cx="7" cy="7" r="7" fill="#444"/><path d="M3.5 6h7v2h-7zM6 3.5h2v7H6z" fill="#fff"/></svg></div></li>
      </ul>
    </div>
    <aside class="aside">
      <div class="card help">
        <h3>Get Help</h3>
        <p>Stuck on a step or unsure how a feature works? Write to our support team and a real person will reply within one working day with clear steps to get you going again.</p>
        <span class="btn">Send mail</span>
      </div>
      <div class="card contact">
        <h3>Contact</h3>
        <ul>
          <li><span class="ico"><svg width="12" height="18" viewBox="0 0 12 18"><rect x="1" y="1" width="10" height="16" rx="2" fill="none" stroke="#fff" stroke-width="2"/></svg></span>1-2345-600-900</li>
          <li><span class="ico"><svg width="18" height="13" viewBox="0 0 18 13"><rect width="18" height="13" rx="1" fill="#fff"/><path d="M0 0 9 7l9-7" fill="none" stroke="#f7931e" stroke-width="1.5"/></svg></span>feedback@pemraq.test</li>
        </ul>
      </div>
    </aside>
  </div>
</section>

<section class="feedback">
  <div class="wrap">
    <blockquote class="quote">
      <div class="mark">“</div>
      <p>I moved all our office records over in an afternoon. Everything stays in our own storage and nobody else can read it, which is exactly...</p>
      <cite>Ravel Domm</cite>
    </blockquote>
    <blockquote class="quote">
      <div class="mark">“</div>
      <p>Finally an encryption tool my whole team can use without training. Setup took minutes and our files open just as fast as before...</p>
      <cite>Isa Fenwold</cite>
    </blockquote>
    <blockquote class="quote">
      <div class="mark">“</div>
      <p>I keep my passwords and notes in one place and sleep better knowing even the service itself cannot look inside my data...</p>
      <cite>Ravel Domm</cite>
    </blockquote>
  </div>
</section>

<footer>
  <nav class="footer-nav">
    <span>Home</span><span>Learn more/FAQ</span><span>Contact</span><span>Log in</span><span>Signup</span>
  </nav>
  <div class="footer-main">
    <div class="social" aria-label="Social links">
      <span style="background:#3b5998"></span><span style="background:#2aa9e0"></span><span style="background:#dd4b39"></span>
    </div>
    <p class="copyright">Copyrights @ 2015 pemraq. All Right Reserveed.</p>
  </div>
  <div class="legal">
    <div class="wrap">
      <h4>Privacy notice</h4>
      <p>We collect only the details needed to run your account, such as your email address and billing records. Your files are encrypted in your browser before they leave your device, and we never hold the keys to read them. We do not sell or share personal data with third parties, except where required by law. You may ask us to export or delete your account information at any time by writing to our support team.</p>
    </div>
    <span class="code">C10</span>
  </div>
</footer>

</body>
</html>
```